Highly rated moving company needs postcard design

We need a highly converting postcard to send when people put their homes for sale online. This should highlight the fact that we're Austin's highest rated moving company, and should convey quality and value. We do local, statewide and long distance moves. We also do office and commerical moves and storage. final design must be sized to work with our mailing system. Please see attached file for more information.

```html
<!DOCTYPE html>
<html lang="en">
<head>
<meta charset="utf-8">
<title>Summit Line Movers – Postcard</title>
<link href="https://fonts.googleapis.com/css2?family=Montserrat:wght@500;600;700;800&family=Oswald:wght@500&display=swap" rel="stylesheet">
<style>
  :root {
    --board: #0e0d24;
    --navy: #1c1868;
    --navy-panel: #262160;
    --red: #f20d0d;
    --white: #ffffff;
    --rule: #9a9a9a;
    --ghost: #ececef;
  }
  * { margin: 0; padding: 0; box-sizing: border-box; }
  html, body { width: 945px; height: 1200px; overflow: hidden; }
  body { background: var(--board); font-family: "Montserrat", sans-serif; position: relative; }

  .card { position: absolute; left: 60px; width: 824px; height: 549px; overflow: hidden; background: var(--white); }
  .card--front { top: 46px; }
  .card--back { top: 608px; }
  .abs { position: absolute; }

  .photo {
    position: absolute; inset: 0;
    clip-path: polygon(496px 0, 824px 0, 824px 549px, 338px 549px);
    background: linear-gradient(135deg, #d9d4cc 0%, #c7a888 35%, #3b52a8 60%, #f2efe9 78%, #b9916c 100%);
  }
  .stripe { position: absolute; inset: 0; background: var(--red); }
  .card--front .stripe { clip-path: polygon(485px 0, 497px 0, 339px 549px, 325px 549px); }

  .brand { text-align: center; font-weight: 700; line-height: 1; }
  .brand__dot { border-radius: 50%; margin: 0 auto; }

  .brand--front { left: 20px; top: 24px; width: 226px; color: var(--red); }
  .brand--front .brand__dot { width: 78px; height: 78px; background: var(--navy); margin-bottom: 12px; }
  .brand--front .brand__name { font-size: 25px; letter-spacing: 2px; }
  .brand--front .brand__sub { font-size: 13px; letter-spacing: 7px; margin-top: 5px; }

  .headline { font-weight: 800; text-transform: uppercase; }
  .headline--front { left: 24px; top: 184px; font-size: 67px; line-height: 58px; letter-spacing: -1.5px; color: var(--navy); }
  .headline--front .accent { color: var(--red); }

  .tagline-band { left: 0; top: 377px; width: 374px; height: 47px; background: var(--navy); color: var(--white); font-size: 12.5px; font-weight: 500; line-height: 14.5px; padding: 9px 0 0 23px; }

  .cta { font-family: "Oswald", sans-serif; font-weight: 500; text-transform: uppercase; line-height: 1; }
  .phone { font-weight: 700; line-height: 1; letter-spacing: -0.5px; }
  .site { font-weight: 500; line-height: 1; }
  .card--front .cta { left: 23px; top: 448px; font-size: 21px; color: var(--navy); letter-spacing: -0.2px; }
  .card--front .phone { left: 22px; top: 473px; font-size: 41px; color: var(--navy); }
  .card--front .site { left: 26px; top: 521px; font-size: 13px; color: var(--navy); }

  .navy-panel { position: absolute; inset: 0; background: var(--navy-panel); clip-path: polygon(0 0, 335px 0, 491px 549px, 0 549px); }
  .card--back .stripe { clip-path: polygon(329px 0, 340px 0, 498px 549px, 484px 549px); }

  .brand--back { left: 10px; top: 22px; width: 156px; color: var(--white); }
  .brand--back .brand__dot { width: 64px; height: 64px; background: var(--white); margin-bottom: 10px; }
  .brand--back .brand__name { font-size: 19px; letter-spacing: 1.5px; }
  .brand--back .brand__sub { font-size: 10px; letter-spacing: 6px; margin-top: 3px; }

  .headline--back { left: 22px; top: 164px; font-size: 44px; line-height: 41px; font-weight: 700; color: var(--white); letter-spacing: -0.5px; }
  .services-note { left: 22px; top: 375px; font-size: 17.5px; font-weight: 600; line-height: 17.5px; color: var(--white); text-transform: uppercase; }
  .card--back .cta { left: 24px; top: 466px; font-size: 17px; color: var(--white); }
  .card--back .phone { left: 22px; top: 486px; font-size: 30px; color: var(--white); }
  .card--back .site { left: 26px; top: 518px; font-size: 11px; color: var(--white); }

  .stamp-box { left: 679px; top: 28px; width: 114px; height: 114px; border: 1.2px solid var(--rule); }
  .address-line { left: 547px; width: 244px; height: 1.2px; background: var(--rule); }

  .brand--ghost { left: 659px; top: 440px; width: 136px; color: var(--ghost); }
  .brand--ghost .brand__dot { width: 50px; height: 50px; background: var(--ghost); margin-bottom: 8px; }
  .brand--ghost .brand__name { font-size: 16px; letter-spacing: 1px; }
  .brand--ghost .brand__sub { font-size: 9px; letter-spacing: 5px; margin-top: 3px; }
</style>
</head>
<body>

<section class="card card--front">
  <div class="photo" role="img" aria-label="Photo of two movers in blue work uniforms loading cardboard boxes into a white van"></div>
  <div class="stripe"></div>

  <div class="brand brand--front abs">
    <div class="brand__dot"></div>
    <div class="brand__name">SUMMIT LINE</div>
    <div class="brand__sub">MOVERS</div>
  </div>

  <h1 class="headline headline--front abs">Fast<br>Relaible<br><span class="accent">Movers</span></h1>

  <p class="tagline-band abs">We're austin's highest rated Moving company,<br>&amp; should Convey quality and value</p>

  <p class="cta abs">Call us today to get started!</p>
  <p class="phone abs">(512) 555-0147</p>
  <p class="site abs">www.summitlinemovers.com</p>
</section>

<section class="card card--back">
  <div class="navy-panel"></div>
  <div class="stripe"></div>

  <div class="brand brand--back abs">
    <div class="brand__dot"></div>
    <div class="brand__name">SUMMIT LINE</div>
    <div class="brand__sub">MOVERS</div>
  </div>

  <h2 class="headline headline--back abs">Local<br>Statewide<br>&amp; Long<br>Distance<br>Moves</h2>
  <p class="services-note abs">We also do office and<br>commerical moves and storage.</p>

  <p class="cta abs">Call us today to get started!</p>
  <p class="phone abs">(512) 555-0147</p>
  <p class="site abs">www.summitlinemovers.com</p>

  <div class="stamp-box abs"></div>
  <div class="address-line abs" style="top:210px"></div>
  <div class="address-line abs" style="top:251px"></div>
  <div class="address-line abs" style="top:292px"></div>

  <div class="brand brand--ghost abs">
    <div class="brand__dot"></div>
    <div class="brand__name">SUMMIT LINE</div>
    <div class="brand__sub">MOVERS</div>
  </div>
</section>

</body>
</html>
```